Need to design a business card with logo

Hellow
we are a company ,
PT REKA LINTAS MANDIRI
looking for design of name card.
what we do is property development and management.
design preferable professional corporate look and feel.
corporate. color, pantone colour 289
information required is
company name " Reka Lintas Mandiri"
person name eg " Peter Hollis"
person title eg "secret agent"
address: 9 kestrel road , jakarta, indonesia
phone : +6221 5906471
mobile : 0813 294 615
email : peter@hollistran.com
website: www.peterhol.com
if you want to include logo in the design you are welcome and appreciated , or you can simply use the company name as the logo.
thanks
corporate , business person , show events, exhibition events ,etc
Business

```html
<!DOCTYPE html>
<html lang="en">
<head>
<meta charset="utf-8">
<title>Peter Hollis – Business Card</title>
<link rel="stylesheet" href="https://fonts.googleapis.com/css2?family=Michroma&family=Tinos:wght@400;700&display=swap">
<style>
  :root {
    --navy: #002349;
    --grey: #b0afae;
    --ink: #000000;
    --paper: #ffffff;
    --display: "Michroma", sans-serif;
    --body: "Tinos", serif;
  }
  * { margin: 0; padding: 0; box-sizing: border-box; }
  html, body { width: 1200px; height: 667px; overflow: hidden; background: var(--paper); }
  .card { position: relative; width: 1200px; height: 667px; background: var(--paper); overflow: hidden; }

  .rule, .stripe { position: absolute; background: var(--navy); }
  .rule-top { left: 0; top: 14px; width: 1200px; height: 6px; }
  .stripe-left { left: 0; width: 590px; }
  .stripe-right { left: 1142px; width: 58px; }
  .stripe-1 { top: 75px; height: 45px; }
  .stripe-2 { top: 133px; height: 28px; }
  .stripe-3 { top: 174px; height: 13px; }

  .nameplate {
    position: absolute; left: 595px; top: 75px; width: 545px; height: 115px;
    background: var(--grey); text-align: center; color: var(--ink);
  }
  .person-name {
    font-family: var(--display); font-size: 38px; letter-spacing: 4px;
    text-transform: uppercase; line-height: 1; margin-top: 18px; font-weight: 400;
    -webkit-text-stroke: 1.2px var(--ink);
  }
  .person-title {
    font-family: var(--display); font-size: 21px; letter-spacing: 3px;
    font-variant: small-caps; line-height: 1; margin-top: 16px;
  }

  .contact { position: absolute; font-family: var(--body); font-size: 30px; color: var(--ink); line-height: 38px; }
  .contact .label { font-weight: 700; }
  .address { left: 40px; top: 266px; }
  .address-lines { position: absolute; left: 145px; top: 0; white-space: nowrap; }
  .details { left: 48px; top: 424px; }
  .details .row { white-space: nowrap; }

  .brand { position: absolute; left: 900px; top: 279px; width: 198px; text-align: center; }
  .brand-mark { display: block; margin: 0 auto; }
  .brand-name {
    font-family: var(--body); font-weight: 700; font-size: 19px; color: var(--navy);
    margin-top: 8px; white-space: nowrap;
  }

  .footer-band {
    position: absolute; left: 0; top: 594px; width: 1200px; height: 56px;
    background: var(--navy); display: flex; align-items: center; justify-content: center;
  }
  .company-name {
    font-family: var(--display); font-size: 22px; letter-spacing: 1px;
    color: var(--paper); text-transform: uppercase; padding-left: 76px;
    -webkit-text-stroke: 0.8px var(--paper);
  }
</style>
</head>
<body>
<div class="card">
  <div class="rule rule-top"></div>
  <div class="stripe stripe-left stripe-1"></div>
  <div class="stripe stripe-left stripe-2"></div>
  <div class="stripe stripe-left stripe-3"></div>
  <div class="stripe stripe-right stripe-1"></div>
  <div class="stripe stripe-right stripe-2"></div>
  <div class="stripe stripe-right stripe-3"></div>

  <div class="nameplate">
    <h1 class="person-name">Peter Hollis</h1>
    <p class="person-title">Secret Agent</p>
  </div>

  <div class="contact address">
    <span class="label">Address</span> :
    <div class="address-lines">9 kestrel road,<br>Jakarta,<br>Indonesia</div>
  </div>

  <div class="contact details">
    <div class="row"><span class="label">Phone</span>&nbsp;&nbsp; : +6221 5906471</div>
    <div class="row"><span class="label">Mobile</span>&nbsp;&nbsp; : 0813 294 615</div>
    <div class="row"><span class="label">email</span>&nbsp;&nbsp;&nbsp;&nbsp; : peter@hollistran.com</div>
    <div class="row"><span class="label">Website</span> : www.peterhol.com</div>
  </div>

  <div class="brand">
    <svg class="brand-mark" width="120" height="120" viewBox="0 0 120 120" aria-hidden="true">
      <circle cx="60" cy="60" r="60" fill="var(--navy)"/>
    </svg>
    <div class="brand-name">Reka Lintas Mandiri</div>
  </div>

  <div class="footer-band">
    <span class="company-name">Reka Lintas Mandiri</span>
  </div>
</div>
</body>
</html>
```